Bottle label design for a mulberry brandy

Please create a label design for a mulberry brandy. The registered brand name is "Tavrik"
The brandy will be produced in Armenia from 100% mulberry.
Color of the product: transparent.
The product will be sold worldwide. The price will be between 30 and 50 USD. So the product will be in premium category.
Therefore we need a solid design, appropriate to the product price category. The design, however, needs to be modern and optimistic.
You can have mulberries on the label or not have, it is up to you.
We have chosen for the product some bottle types, the links to the available bottles you can find in the attachment. Ideally you show a picture of your label on the bottle you selected.

worldwide

```html
<!DOCTYPE html>
<html lang="en">
<head>
<meta charset="utf-8">
<title>Tavrik Mulberry Brandy – Label</title>
<link rel="stylesheet" href="https://fonts.googleapis.com/css2?family=Playfair+Display:wght@700;900&family=Alfa+Slab+One&family=Roboto+Slab:wght@100..900&family=Pinyon+Script&family=Montserrat:wght@400;500&display=swap">
<style>
  :root {
    --page: #e9e9e9;
    --label-deep: #3a1216;
    --label-mid: #4d1a1f;
    --tile-line: rgba(150, 120, 160, 0.28);
    --tile-fill: rgba(90, 60, 90, 0.18);
    --copper: #d9864a;
    --copper-light: #f0a86a;
    --gold: #f2b453;
    --cream: #fbf4ea;
  }
  * { margin: 0; padding: 0; box-sizing: border-box; }
  html, body { width: 1200px; height: 1027px; overflow: hidden; background: var(--page); }
  .canvas { position: relative; width: 1200px; height: 1027px; }
  .label {
    position: absolute; left: 272px; top: 63px; width: 656px; height: 900px;
    background: var(--label-deep); overflow: hidden;
  }
  .label-pattern {
    position: absolute; inset: 0;
    background:
      repeating-linear-gradient(90deg, var(--tile-line) 0 2px, transparent 2px 70px),
      repeating-linear-gradient(0deg, var(--tile-line) 0 2px, transparent 2px 70px),
      radial-gradient(ellipse at 50% 45%, #5a2630 0%, var(--label-mid) 50%, var(--label-deep) 100%);
    background-position: 8px 8px, 8px 8px, 0 0;
  }
  .label-pattern::after {
    content: ""; position: absolute; inset: 0;
    background:
      repeating-linear-gradient(90deg, transparent 0 10px, var(--tile-fill) 10px 60px, transparent 60px 70px);
    background-position: 8px 0;
    mask: repeating-linear-gradient(0deg, transparent 0 10px, #000 10px 60px, transparent 60px 70px);
    -webkit-mask: repeating-linear-gradient(0deg, transparent 0 10px, #000 10px 60px, transparent 60px 70px);
    -webkit-mask-position: 0 8px; mask-position: 0 8px;
  }
  .frame { position: absolute; inset: 0; }
  .brand {
    position: absolute; top: 104px; left: 0; width: 100%; text-align: center;
    font-family: "Playfair Display", serif; font-weight: 900; font-size: 70px;
    line-height: 1; color: var(--cream); letter-spacing: 1px;
  }
  .variety {
    position: absolute; top: 312px; left: 0; width: 100%; text-align: center;
    font-family: "Alfa Slab One", serif; font-size: 54px; line-height: 1;
    color: var(--gold); letter-spacing: 1px;
  }
  .category {
    position: absolute; top: 420px; left: 0; width: 100%; text-align: center;
    font-family: "Roboto Slab", serif; font-weight: 800; font-size: 92px; line-height: 1;
    color: var(--copper-light); letter-spacing: 18px; padding-left: 18px;
  }
  .composition {
    position: absolute; top: 526px; left: 0; width: 100%; text-align: center;
    font-family: "Montserrat", sans-serif; font-size: 26px; color: var(--cream);
  }
  .origin {
    position: absolute; top: 628px; left: 0; width: 100%; text-align: center;
    font-family: "Pinyon Script", cursive; font-size: 44px; color: var(--cream);
  }
  .specs {
    position: absolute; left: 66px; top: 715px; width: 524px; height: 132px;
    display: flex; align-items: center;
    font-family: "Montserrat", sans-serif; color: var(--cream);
  }
  .specs .volume { flex: 1; text-align: center; font-size: 34px; font-weight: 500; }
  .specs .abv { flex: 1; text-align: center; font-size: 27px; }
  .specs .divider { width: 3px; height: 60px; background: var(--copper); }
</style>
</head>
<body>
<main class="canvas">
  <section class="label">
    <div class="label-pattern" role="img" aria-label="Grid of traditional Armenian geometric tile patterns in muted plum and grey lines"></div>
    <svg class="frame" width="656" height="900" viewBox="0 0 656 900" fill="none" stroke="#d9864a" stroke-width="3">
      <line x1="70" y1="44" x2="286" y2="44"/>
      <line x1="370" y1="44" x2="586" y2="44"/>
      <line x1="90" y1="54" x2="566" y2="54" stroke-width="1.5"/>
      <path d="M328 28 L350 44 L328 60 L306 44 Z"/>
      <path d="M90 100 l8 -8 l8 8 l-8 8 Z M550 100 l8 -8 l8 8 l-8 8 Z" fill="#d9864a"/>
      <line x1="110" y1="150" x2="175" y2="150"/>
      <line x1="110" y1="160" x2="175" y2="160"/>
      <line x1="481" y1="150" x2="546" y2="150"/>
      <line x1="481" y1="160" x2="546" y2="160"/>
      <path d="M175 184 L29 184 L29 692 L627 692 L627 184 L481 184"/>
      <rect x="41" y="196" width="574" height="484" stroke-width="1.5"/>
      <line x1="150" y1="398" x2="316" y2="398" stroke-width="1.5"/>
      <line x1="340" y1="398" x2="506" y2="398" stroke-width="1.5"/>
      <path d="M328 392 l6 6 l-6 6 l-6 -6 Z" stroke-width="1.5"/>
      <rect x="66" y="715" width="524" height="132"/>
      <rect x="76" y="725" width="504" height="112" stroke-width="1.5"/>
    </svg>
    <h1 class="brand">TAVRIK</h1>
    <p class="variety">MULBERRY</p>
    <p class="category">BRANDY</p>
    <p class="composition">100% MULBERRY</p>
    <p class="origin">Produced in Armenia</p>
    <div class="specs">
      <span class="volume">700ml</span>
      <span class="divider"></span>
      <span class="abv">42% Alc/Vol</span>
    </div>
  </section>
</main>
</body>
</html>
```